Birchwell Craft House business card design- Fine Art sculpture business (Contract guaranteed)

This business card is for a fine art business. Though we don't have a website up and running yet it should be up soon. I would like the business card to be elegant and fairly simple with a picture of one of my sculptures on the front (you might need to photoshop out the background) as well as my basic contact info (my name,phone # and e-mail). On the back I'd like it to be pretty simple with just "Notes" and some blank lines for writing in info.
Updates

Target Market(s)

High end artwork buyers

Industry/Entity Type

Art Gallery

Contact Information for Business Card

Wendell Marsh Phone: (555) 312-4098 E-mail: wendell@quarrymint.example Facebook: @birchwellcrafthouse Instagram: birchwellcrafthouse

Colors

Designer to choose colors to be used in the design.

Requirements
Must have
• *A picture of one of my sculptures*, my name, business name (Birchwell Craft House), e-mail, phone #, and a notes section on the back.
• Birchwell Craft House
• Wendell Marsh
• (555)312-4098
• wendell@quarrymint.example
• Facebook: @birchwellcrafthouse
• Instagram: birchwellcrafthouse
Nice to have
• It'd be nice if you can crop out the background in the sculpture pictures, which ever one you end up using.

```html
<!DOCTYPE html>
<html lang="en">
<head>
<meta charset="utf-8">
<title>Birchwell Craft House — Notes Card</title>
<link rel="stylesheet" href="https://fonts.googleapis.com/css2?family=Alegreya:wght@400&display=swap">
<style>
  :root {
    --ink: #111111;
    --paper: #ffffff;
    --band: #2c1548;
    --rule: #1a1a1a;
  }
  html, body {
    margin: 0;
    padding: 0;
    width: 1200px;
    height: 667px;
    overflow: hidden;
    background: var(--paper);
  }
  .card-back {
    position: relative;
    width: 1200px;
    height: 667px;
    background: var(--paper);
    overflow: hidden;
  }
  .top-band {
    position: absolute;
    top: 0;
    left: 0;
    width: 100%;
    height: 17px;
    background: var(--band);
  }
  .notes-label {
    position: absolute;
    left: 87px;
    top: 148px;
    margin: 0;
    font-family: "Alegreya", Georgia, serif;
    font-weight: 400;
    font-size: 41px;
    line-height: 1;
    color: var(--ink);
    letter-spacing: 0.5px;
  }
  .writing-lines {
    position: absolute;
    left: 221px;
    top: 0;
    width: 856px;
    height: 667px;
  }
</style>
</head>
<body>
  <main class="card-back">
    <div class="top-band"></div>
    <h1 class="notes-label">Notes:</h1>
    <svg class="writing-lines" viewBox="0 0 856 667" width="856" height="667" aria-hidden="true">
      <g stroke="var(--rule)" stroke-width="1.3">
        <line x1="0" y1="182" x2="856" y2="182"/>
        <line x1="0" y1="225" x2="856" y2="225"/>
        <line x1="0" y1="264" x2="856" y2="264"/>
        <line x1="0" y1="307" x2="856" y2="307"/>
        <line x1="0" y1="352" x2="856" y2="352"/>
        <line x1="0" y1="395" x2="856" y2="395"/>
        <line x1="0" y1="440" x2="856" y2="440"/>
        <line x1="0" y1="484" x2="856" y2="484"/>
        <line x1="0" y1="524" x2="856" y2="524"/>
        <line x1="0" y1="566" x2="856" y2="566"/>
      </g>
    </svg>
  </main>
</body>
</html>
```